Business card design and logo needed

We have been operating as Ridgeline Posts for 30 years but never had a logo and feel there is a need for one, but have no idea for a design.
We specialise in all types of rural fencing including post and wire, post and rail, electric, chainmesh and to a lesser extent, also do industrial security fencing.
Updates

Sorry, but website is ridgelineposts.example

No .au on the end!
My apologies

Regards, Darren

Target Market(s)

Rural/acreage property owners, particularly horse people.

Industry/Entity Type

Industrial

Contact Information for Business Card

Ridgeline Posts Darren Kellett 0499 572106. Lewis Kellett 0499 613720
Email: ridgelineposts@mailhub.example
Website: www.ridgelineposts.example

Requirements
Must have
• Would like to highlight website address - use the business card to advertise the website or to push them to check it out.

```html
<!DOCTYPE html>
<html lang="en">
<head>
<meta charset="utf-8">
<title>Ridgeline Posts – Business Card</title>
<link rel="stylesheet" href="https://fonts.googleapis.com/css2?family=Crimson+Pro:wght@400;700&display=swap">
<style>
  :root {
    --page-bg: #ffffff;
    --card-bg: #ffffff;
    --card-border: #2b2b2b;
    --accent-circle: #ebf1d6;
    --contact-text: #7b7f78;
    --website-text: #636466;
    --scene-light: #e3e4e5;
    --scene-dark: #cfd0d2;
  }
  html, body {
    margin: 0;
    padding: 0;
    width: 1200px;
    height: 1000px;
    overflow: hidden;
    background: var(--page-bg);
  }
  .canvas {
    position: relative;
    width: 1200px;
    height: 1000px;
  }
  .business-card {
    position: absolute;
    left: 121px;
    top: 201px;
    width: 1025px;
    height: 576px;
    border: 1.5px solid var(--card-border);
    background: var(--card-bg);
    overflow: hidden;
  }
  .accent-circle {
    position: absolute;
    left: -309px;
    top: -228px;
    width: 660px;
    height: 660px;
    border-radius: 50%;
    background: var(--accent-circle);
  }
  .contact-list {
    position: absolute;
    left: 52px;
    top: 38px;
    margin: 0;
    padding: 0;
    list-style: none;
    font-family: "Crimson Pro", "Minion Pro", Georgia, serif;
    font-weight: 400;
    font-size: 34px;
    line-height: 48px;
    color: var(--contact-text);
  }
  .farm-scene {
    position: absolute;
    left: 266px;
    top: 186px;
    width: 554px;
    height: 220px;
  }
  .website {
    position: absolute;
    left: 40px;
    right: 40px;
    top: 440px;
    margin: 0;
    text-align: center;
    white-space: nowrap;
    font-family: "Crimson Pro", "Minion Pro", Georgia, serif;
    font-weight: 700;
    font-size: 68px;
    line-height: 90px;
    letter-spacing: -0.5px;
    color: var(--website-text);
  }
</style>
</head>
<body>
  <main class="canvas">
    <section class="business-card">
      <div class="accent-circle"></div>

      <ul class="contact-list">
        <li class="contact-person">Darren Kellett 0499 572106</li>
        <li class="contact-person">Lewis Kellett 0499 613720</li>
        <li class="contact-email">Email: ridgelineposts@mailhub.example</li>
      </ul>

      <svg class="farm-scene" viewBox="0 0 554 220" role="img"
           aria-label="Illustration of a horse beside a post and rail fence in front of a stable">
        <defs>
          <linearGradient id="scene-tone" x1="0" y1="0" x2="0" y2="1">
            <stop offset="0" stop-color="var(--scene-light)"/>
            <stop offset="1" stop-color="var(--scene-dark)"/>
          </linearGradient>
        </defs>
        <rect x="0" y="0" width="554" height="220" rx="6" fill="url(#scene-tone)"/>
      </svg>

      <p class="website">www.ridgelineposts.example</p>
    </section>
  </main>
</body>
</html>
```